Business Card for a Little Gothic Online Shoe Business
Velvet Moth Treasures
Business Card for a Little Gothic Online Shoe Business - Apparel
Creative Brief
Bright & Fun-filled
9 Carrowby Street Kelvin Flats QLD 4826
velvetmothtreasures@mailbrook.net
www.velvetmothtreasures-shop.com.au
ABN: 41 285 607 952
In addition to Business card designs I would also like to see designs for Letterhead and Envelope.
This should be a really funky fresh design to match the Business Logo. Our Colours are Purple and Black but Im open to others as long as the Business Logo is not changed. I also like the idea of incorpating Candy Striping or Old Victorian Floral Motifs in the Card I do not want any Shoes on the card as we also do Clothes etc

```html
<!DOCTYPE html>
<html lang="en">
<head>
<meta charset="utf-8">
<title>Velvet Moth Treasures – Stationery Set</title>
<link href="https://fonts.googleapis.com/css2?family=Montserrat:wght@400;700&family=Great+Vibes&display=swap" rel="stylesheet">
<style>
:root{
  --purple:#5b21a8;
  --purple-dark:#3b0f72;
  --ink:#141414;
  --paper:#ffffff;
  --line:#d9d2e6;
  --muted:#8a8a8a;
  --ghost:#eeeaf3;
  --bg:#ffffff;
}
*{box-sizing:border-box;margin:0;padding:0}
html,body{width:1200px;height:230px;overflow:hidden;background:var(--bg)}
body{position:relative;font-family:"Montserrat",Arial,sans-serif;color:var(--ink)}
.item{position:absolute;background:var(--paper);box-shadow:0 1px 3px rgba(0,0,0,.35);overflow:hidden}
.wave{position:absolute;left:0;bottom:0;width:100%}
.mark{display:flex;align-items:center;gap:2px;font-weight:700;color:var(--purple);white-space:nowrap}
.mark .dot{border-radius:50%;background:var(--purple);flex:none}
.tiny{font-size:2.4px;color:var(--muted);line-height:1.4;white-space:nowrap}

/* business cards */
.card{width:54px;height:31px}
.card--dark{background:var(--ink)}
.card--dark .mark{color:var(--paper)}
.card--dark .mark .dot{background:var(--paper)}
.card--purple{background:var(--purple)}
.card--purple .mark{color:var(--paper)}
.card--purple .mark .dot{background:var(--paper)}
.card .mark{position:absolute;left:4px;top:5px;font-size:3.4px}
.card .mark .dot{width:5px;height:5px}
.card .tiny{position:absolute;left:4px;top:13px}
.card--dark .tiny,.card--purple .tiny{color:#ddd}

/* letterhead */
.sheet{width:132px;height:192px;top:19px}
.sheet .mark{position:absolute;left:50%;transform:translateX(-50%);top:7px;font-size:5px}
.sheet .mark .dot{width:8px;height:8px}
.ghost-art{position:absolute;left:36px;top:62px;width:60px;height:56px;border-radius:45% 45% 40% 40%;background:radial-gradient(circle,var(--ghost),#f7f5fa)}

/* invoice */
.invoice .mark{left:8px;transform:none}
.invoice-title{position:absolute;right:8px;top:8px;font-size:5px;font-weight:700;color:var(--purple);letter-spacing:.3px}
.invoice-meta{position:absolute;left:8px;top:22px}
.invoice-meta.right{left:auto;right:8px;text-align:right}
.invoice-table{position:absolute;left:8px;top:42px;border-collapse:collapse;font-size:2.4px;width:116px}
.invoice-table th{background:var(--purple);color:var(--paper);height:5px;font-weight:700;text-align:left;padding-left:2px}
.invoice-table td{height:5.2px;border-bottom:.4px solid var(--line)}
.invoice-table td+td,.invoice-table th+th{border-left:.4px solid var(--line)}
.totals{position:absolute;right:8px;top:142px;width:44px;font-size:2.4px}
.totals div{display:flex;justify-content:space-between;border-bottom:.4px solid var(--line);height:5px;align-items:center;padding:0 2px}
.totals .grand{background:var(--purple);color:var(--paper);font-weight:700}

/* compliments slip */
.slip{left:833px;top:14px;width:139px;height:77px}
.slip .mark{position:absolute;left:6px;top:6px;font-size:4px}
.slip .mark .dot{width:6px;height:6px}
.slip-script{position:absolute;left:56px;top:14px;font-family:"Great Vibes",cursive;font-size:11px;color:var(--purple)}

/* envelopes */
.envelope{width:214px;height:70px}
.envelope .flap{position:absolute;inset:0;width:100%;height:100%}
.envelope .mark{position:absolute;left:8px;top:40px;font-size:4px}
.envelope .mark .dot{width:6px;height:6px}
</style>
</head>
<body>

<!-- business cards: dark backs -->
<div class="item card card--dark" style="left:7px;top:53px">
  <div class="mark"><span class="dot"></span>Velvet Moth Treasures</div>
  <svg class="wave" viewBox="0 0 100 30" preserveAspectRatio="none" height="12"><path d="M0 10C30 30 60 0 100 12V30H0Z" fill="var(--purple)"/></svg>
</div>
<div class="item card card--dark" style="left:7px;top:101px">
  <div class="mark"><span class="dot"></span>Velvet Moth Treasures</div>
  <p class="tiny">Shop Owner</p>
  <svg class="wave" viewBox="0 0 100 30" preserveAspectRatio="none" height="12"><path d="M0 10C30 30 60 0 100 12V30H0Z" fill="var(--purple)"/></svg>
</div>
<div class="item card card--dark" style="left:7px;top:149px">
  <div class="mark"><span class="dot"></span>Velvet Moth Treasures</div>
  <svg class="wave" viewBox="0 0 100 30" preserveAspectRatio="none" height="12"><path d="M0 10C30 30 60 0 100 12V30H0Z" fill="var(--purple)"/></svg>
</div>

<!-- business cards: fronts -->
<div class="item card" style="left:72px;top:53px">
  <div class="mark"><span class="dot"></span>Velvet Moth Treasures</div>
  <p class="tiny">velvetmothtreasures@mailbrook.net<br>www.velvetmothtreasures-shop.com.au</p>
  <svg class="wave" viewBox="0 0 100 30" preserveAspectRatio="none" height="9"><path d="M0 12C30 30 60 -2 100 10V30H0Z" fill="var(--purple)"/><path d="M0 20C35 34 65 6 100 18V30H0Z" fill="var(--ink)"/></svg>
</div>
<div class="item card card--purple" style="left:72px;top:101px">
  <div class="mark"><span class="dot"></span>Velvet Moth Treasures</div>
  <p class="tiny">9 Carrowby Street Kelvin Flats QLD 4826<br>ABN: 41 285 607 952</p>
  <svg class="wave" viewBox="0 0 100 30" preserveAspectRatio="none" height="9"><path d="M0 14C35 32 65 2 100 16V30H0Z" fill="var(--ink)"/></svg>
</div>
<div class="item card" style="left:72px;top:149px">
  <div class="mark"><span class="dot"></span>Velvet Moth Treasures</div>
  <p class="tiny">Shop Owner<br>velvetmothtreasures@mailbrook.net</p>
  <svg class="wave" viewBox="0 0 100 30" preserveAspectRatio="none" height="9"><path d="M0 12C30 30 60 -2 100 10V30H0Z" fill="var(--purple)"/><path d="M0 20C35 34 65 6 100 18V30H0Z" fill="var(--ink)"/></svg>
</div>

<!-- letterheads -->
<div class="item sheet" style="left:151px">
  <div class="mark"><span class="dot"></span>Velvet Moth Treasures</div>
  <div class="ghost-art" role="img" aria-label="Faint brand emblem watermark"></div>
  <svg class="wave" viewBox="0 0 100 30" preserveAspectRatio="none" height="22"><path d="M0 12C30 30 60 -2 100 10V30H0Z" fill="var(--purple)"/><path d="M0 20C35 34 65 6 100 18V30H0Z" fill="var(--ink)"/></svg>
</div>
<div class="item sheet" style="left:300px">
  <div class="mark"><span class="dot"></span>Velvet Moth Treasures</div>
  <div class="ghost-art" role="img" aria-label="Faint brand emblem watermark"></div>
  <svg class="wave" viewBox="0 0 100 30" preserveAspectRatio="none" height="22"><path d="M0 12C30 30 60 -2 100 10V30H0Z" fill="var(--purple)"/><path d="M0 20C35 34 65 6 100 18V30H0Z" fill="var(--ink)"/></svg>
</div>

<!-- invoices -->
<div class="item sheet invoice" style="left:480px">
  <div class="mark"><span class="dot"></span>Velvet Moth Treasures</div>
  <div class="invoice-title">TAX INVOICE</div>
  <p class="tiny invoice-meta">Bill To<br>Date</p>
  <p class="tiny invoice-meta right">Invoice No<br>ABN: 41 285 607 952</p>
  <table class="invoice-table">
    <tr><th style="width:14px">Qty</th><th>Description</th><th style="width:20px">Price</th><th style="width:22px">Amount</th></tr>
    <tr><td></td><td></td><td></td><td></td></tr><tr><td></td><td></td><td></td><td></td></tr>
    <tr><td></td><td></td><td></td><td></td></tr><tr><td></td><td></td><td></td><td></td></tr>
    <tr><td></td><td></td><td></td><td></td></tr><tr><td></td><td></td><td></td><td></td></tr>
    <tr><td></td><td></td><td></td><td></td></tr><tr><td></td><td></td><td></td><td></td></tr>
    <tr><td></td><td></td><td></td><td></td></tr><tr><td></td><td></td><td></td><td></td></tr>
    <tr><td></td><td></td><td></td><td></td></tr><tr><td></td><td></td><td></td><td></td></tr>
    <tr><td></td><td></td><td></td><td></td></tr><tr><td></td><td></td><td></td><td></td></tr>
    <tr><td></td><td></td><td></td><td></td></tr><tr><td></td><td></td><td></td><td></td></tr>
  </table>
  <div class="totals"><div><span>Subtotal</span></div><div><span>GST</span></div><div class="grand"><span>Total</span></div></div>
  <svg class="wave" viewBox="0 0 100 30" preserveAspectRatio="none" height="22"><path d="M0 12C30 30 60 -2 100 10V30H0Z" fill="var(--purple)"/><path d="M0 20C35 34 65 6 100 18V30H0Z" fill="var(--ink)"/></svg>
</div>
<div class="item sheet invoice" style="left:682px">
  <div class="mark"><span class="dot"></span>Velvet Moth Treasures</div>
  <div class="invoice-title">TAX INVOICE</div>
  <p class="tiny invoice-meta">Bill To<br>Date</p>
  <p class="tiny invoice-meta right">Invoice No<br>ABN: 41 285 607 952</p>
  <table class="invoice-table">
    <tr><th style="width:14px">Qty</th><th>Description</th><th style="width:20px">Price</th><th style="width:22px">Amount</th></tr>
    <tr><td></td><td></td><td></td><td></td></tr><tr><td></td><td></td><td></td><td></td></tr>
    <tr><td></td><td></td><td></td><td></td></tr><tr><td></td><td></td><td></td><td></td></tr>
    <tr><td></td><td></td><td></td><td></td></tr><tr><td></td><td></td><td></td><td></td></tr>
    <tr><td></td><td></td><td></td><td></td></tr><tr><td></td><td></td><td></td><td></td></tr>
    <tr><td></td><td></td><td></td><td></td></tr><tr><td></td><td></td><td></td><td></td></tr>
    <tr><td></td><td></td><td></td><td></td></tr><tr><td></td><td></td><td></td><td></td></tr>
    <tr><td></td><td></td><td></td><td></td></tr><tr><td></td><td></td><td></td><td></td></tr>
    <tr><td></td><td></td><td></td><td></td></tr><tr><td></td><td></td><td></td><td></td></tr>
  </table>
  <div class="totals"><div><span>Subtotal</span></div><div><span>GST</span></div><div class="grand"><span>Total</span></div></div>
  <svg class="wave" viewBox="0 0 100 30" preserveAspectRatio="none" height="22"><path d="M0 12C30 30 60 -2 100 10V30H0Z" fill="var(--purple)"/><path d="M0 20C35 34 65 6 100 18V30H0Z" fill="var(--ink)"/></svg>
</div>

<!-- compliments slip -->
<div class="item slip">
  <div class="mark"><span class="dot"></span>Velvet Moth Treasures</div>
  <div class="slip-script">With Compliments</div>
  <svg class="wave" viewBox="0 0 100 30" preserveAspectRatio="none" height="14"><path d="M0 12C30 30 60 -2 100 10V30H0Z" fill="var(--purple)"/><path d="M0 20C35 34 65 6 100 18V30H0Z" fill="var(--ink)"/></svg>
</div>

<!-- small card below slip -->
<div class="item card" style="left:833px;top:104px;width:68px;height:38px">
  <div class="mark"><span class="dot"></span>Velvet Moth Treasures</div>
  <p class="tiny">www.velvetmothtreasures-shop.com.au</p>
  <svg class="wave" viewBox="0 0 100 30" preserveAspectRatio="none" height="10"><path d="M0 12C30 30 60 -2 100 10V30H0Z" fill="var(--purple)"/><path d="M0 20C35 34 65 6 100 18V30H0Z" fill="var(--ink)"/></svg>
</div>

<!-- envelopes -->
<div class="item envelope" style="left:979px;top:26px">
  <svg class="flap" viewBox="0 0 214 70" preserveAspectRatio="none">
    <path d="M0 0L107 38L214 0Z" fill="var(--ink)"/>
    <path d="M0 0L107 32L214 0Z" fill="var(--purple)"/>
    <path d="M0 70L80 36M214 70L134 36" stroke="var(--line)" stroke-width=".6" fill="none"/>
  </svg>
</div>
<div class="item envelope" style="left:979px;top:113px">
  <div class="mark"><span class="dot"></span>Velvet Moth Treasures</div>
  <svg class="wave" viewBox="0 0 100 30" preserveAspectRatio="none" height="12"><path d="M0 12C30 30 60 -2 100 10V30H0Z" fill="var(--purple)"/><path d="M0 20C35 34 65 6 100 18V30H0Z" fill="var(--ink)"/></svg>
</div>

</body>
</html>
```